Bottlecap Decals Inc. NEED DESIGNS FOR THE HOLIDAY STICKERS

We need 6 designs for the HOLIDAY SET of Bottlecap Decals. I have attached some imagery that we like as well as the flagship pack of stickers that were also designed by you AWESOME DESIGNERS!! You are not limited to this imagery, it is only to show you what style we like but remember, YOU ARE THE ARTIST! Each design needs to have a "TO: & FROM:" for people to write in their name and the recipients name. We need designs for the following occasions:

1. HALLOWEEN
2. HAPPY HOLIDAYS (THANKSGIVING, CHRISTMAS, WINTER, LEAVES)
3. ST. PATRICK'S DAY
4. "LET'S CELEBRATE" PATRIOTIC THEME (JULY 4TH, VETERANS DAY, MEMORIAL DAY COMBINED)
5. HAPPY NEW YEAR
6. SUMMER THEME GENERIC

***these 6 designs must fit on one of die cut shapes which are included in the brief***

**PLEASE SUBMIT YOUR IDEA FOR AS MANY DESIGNS AS YOU CAN (PREFERABLY ALL 6). WE NEED 6 DESIGNS SO IF 4 OF YOURS ARE GOOD AND 2 OF ANOTHERS ARE GOOD, YOU WOULD WIN 1ST AND THEY WOULD WIN 2ND.

Font styles to use
Serif
Sans Serif
Decorative
Script

Requirements
Must have
• - lines for "to" and "from"
• - must fit on a die cut shape (provided)
• - must be FUN and colorful!!
Nice to have
• color, imagery, fun!

```html
<!DOCTYPE html>
<html lang="en">
<head>
<meta charset="UTF-8">
<title>Saint Patrick's Day Gift Sticker</title>
<link rel="stylesheet" href="https://fonts.googleapis.com/css2?family=Orbitron:wght@800;900&family=Oswald:wght@500&display=swap">
<style>
  :root {
    --page: #ffffff;
    --stone-light: #d6cdb9;
    --stone-pale: #e2dac8;
    --stone-mid: #b0a68f;
    --stone-deep: #5e5649;
    --stone-dark: #1f1c18;
    --mug-shade: #5d574c;
    --mug-light: #9c9483;
    --ink: #2a241d;
    --label-text: #ffffff;
  }
  html, body {
    margin: 0;
    padding: 0;
    width: 968px;
    height: 1200px;
    overflow: hidden;
    background: var(--page);
  }
  .sticker {
    display: block;
    width: 968px;
    height: 1200px;
  }
  .title-saint {
    font-family: "Orbitron", sans-serif;
    font-weight: 900;
    font-size: 130px;
    fill: var(--ink);
  }
  .title-occasion {
    font-family: "Orbitron", sans-serif;
    font-weight: 800;
    font-size: 74px;
    fill: var(--ink);
  }
  .field-label {
    font-family: "Oswald", sans-serif;
    font-weight: 500;
    font-size: 34px;
    fill: var(--label-text);
  }
  .field-line {
    stroke: var(--label-text);
    stroke-width: 3;
  }
</style>
</head>
<body>
<svg class="sticker" viewBox="0 0 968 1200" xmlns="http://www.w3.org/2000/svg">
  <defs>
    <clipPath id="die-cut">
      <path d="M232,236 Q485,104 738,236 Q750,335 848,344 L848,846 Q750,855 747,954 Q485,1094 224,954 Q220,855 126,846 L126,344 Q220,335 232,236 Z"/>
    </clipPath>
    <linearGradient id="stone-fill" x1="0" y1="0" x2="0" y2="1">
      <stop offset="0" stop-color="var(--stone-mid)"/>
      <stop offset="0.22" stop-color="var(--stone-light)"/>
      <stop offset="0.45" stop-color="var(--stone-pale)"/>
      <stop offset="0.66" stop-color="var(--stone-mid)"/>
      <stop offset="0.76" stop-color="var(--stone-deep)"/>
      <stop offset="0.86" stop-color="var(--stone-dark)"/>
      <stop offset="1" stop-color="var(--stone-dark)"/>
    </linearGradient>
    <linearGradient id="mugs-fill" x1="0" y1="0" x2="0" y2="1">
      <stop offset="0" stop-color="var(--mug-light)"/>
      <stop offset="0.55" stop-color="var(--mug-shade)"/>
      <stop offset="1" stop-color="var(--mug-light)"/>
    </linearGradient>
  </defs>

  <g class="die-cut" clip-path="url(#die-cut)">
    <rect class="stone-texture" x="120" y="100" width="740" height="1000" fill="url(#stone-fill)" role="img" aria-label="Rough sandstone texture background"/>
    <rect class="mugs-illustration" x="368" y="240" width="280" height="258" rx="28" fill="url(#mugs-fill)" role="img" aria-label="Two foaming beer mugs clinking in a toast"/>

    <text class="title-saint" x="487" y="620" text-anchor="middle" textLength="491" lengthAdjust="spacingAndGlyphs">SAINT</text>
    <text class="title-occasion" x="493" y="707" text-anchor="middle" textLength="678" lengthAdjust="spacingAndGlyphs">PATRICK'S DAY</text>

    <text class="field-label" x="320" y="882">TO:</text>
    <line class="field-line" x1="387" y1="879" x2="642" y2="879"/>
    <text class="field-label" x="320" y="940">FROM:</text>
    <line class="field-line" x1="416" y1="937" x2="642" y2="937"/>
  </g>
</svg>
</body>
</html>
```